electrical contractor business card for professional modern company

I need a business card design for an electrical contractors business. I do all kinds of electricical work from new homes, air conditioning, data and communications. I have a logo design i want on it and have a good idea in my head of what i want it to look like. I like simple yet bold and professional looking. All black background is a must

Target Market(s)

Anyone needing electrical work done

Industry/Entity Type

Electrical

Contact Information for Business Card

company name- KTW Electrical and Data
person name-martin pellowe
phone number- 0418 362 927
website-ktwelec.example.com.au

Font styles to use
Sans Serif

Requirements
Must have
• email
• website
• logo
• name
• phone number
• list of work i do:
• -electrical
• -air-conditioning
• -data/communications
• -cctv/security
• -domestic/commercial/industrial
• -24hr emergency breakdown repair
Nice to have
• i would like the logo on the front side in the centre taking up most of the card with black background.
• on the rear i want the list of work i do with company info i.e. email, website, my name, phone number. rear of card also black background with orange writing to match the orange in the logo

```html
<!DOCTYPE html>
<html lang="en">
<head>
<meta charset="utf-8">
<title>KTW Electrical and Data – Business Card</title>
<link href="https://fonts.googleapis.com/css2?family=Carlito:wght@400;700&display=swap" rel="stylesheet">
<style>
  :root {
    --page: #ffffff;
    --card: #120e0d;
    --orange: #ee7a3f;
    --orange-soft: #c96f43;
    --haze: rgba(120, 120, 120, 0.28);
    --divider: #f2f2f2;
  }
  * { margin: 0; padding: 0; box-sizing: border-box; }
  html, body {
    width: 1200px;
    height: 1000px;
    overflow: hidden;
    background: var(--page);
    font-family: "Carlito", "Calibri", sans-serif;
  }
  .sheet { position: relative; width: 1200px; height: 1000px; }

  .card {
    position: absolute;
    width: 722px;
    height: 422px;
    background: var(--card);
    overflow: hidden;
  }
  .card--front { left: 48px; top: 38px; }
  .card--back { left: 429px; top: 523px; }

  .sheet-divider {
    position: absolute;
    left: 240px;
    top: 472px;
    width: 720px;
    height: 1px;
    background: var(--divider);
  }

  /* Front */
  .brand-lockup {
    position: absolute;
    left: 0;
    right: 0;
    top: 178px;
    display: flex;
    align-items: center;
    justify-content: center;
    gap: 18px;
  }
  .brand-dot {
    width: 34px;
    height: 34px;
    border-radius: 50%;
    background: var(--orange);
  }
  .brand-name {
    color: var(--orange);
    font-weight: 700;
    font-size: 50px;
    letter-spacing: 0.5px;
    line-height: 1;
  }

  /* Back */
  .name-haze {
    position: absolute;
    left: 10px;
    top: 50px;
    width: 702px;
    height: 80px;
    background: radial-gradient(ellipse at center, var(--haze) 0%, rgba(120,120,120,0.12) 55%, rgba(0,0,0,0) 75%);
  }
  .holder-name {
    position: absolute;
    left: 55px;
    top: 48px;
    color: var(--orange);
    font-size: 37px;
    font-weight: 400;
  }
  .brand-mini {
    position: absolute;
    right: 56px;
    top: 70px;
    color: var(--orange);
    font-weight: 700;
    font-size: 14px;
  }
  .name-rule {
    position: absolute;
    left: 52px;
    top: 101px;
    width: 618px;
    height: 2px;
    background: var(--orange);
  }
  .sectors {
    position: absolute;
    left: 0;
    right: 0;
    top: 127px;
    text-align: center;
    color: var(--orange);
    font-size: 28px;
  }
  .services {
    position: absolute;
    top: 197px;
    left: 103px;
    display: grid;
    grid-template-columns: 300px 260px;
    row-gap: 4px;
    list-style: none;
    color: var(--orange-soft);
    font-size: 21px;
    line-height: 25px;
  }
  .contact {
    position: absolute;
    left: 0;
    right: 0;
    top: 339px;
    text-align: center;
    color: var(--orange);
    font-size: 14.5px;
    line-height: 19px;
  }
</style>
</head>
<body>
<main class="sheet">
  <section class="card card--front" aria-label="Card front">
    <div class="brand-lockup">
      <span class="brand-dot"></span>
      <span class="brand-name">KTW Electrical and Data</span>
    </div>
  </section>

  <div class="sheet-divider"></div>

  <section class="card card--back" aria-label="Card back">
    <div class="name-haze"></div>
    <h1 class="holder-name">Martin Pellowe</h1>
    <span class="brand-mini">KTW Electrical and Data</span>
    <div class="name-rule"></div>
    <p class="sectors">Domestic - Commercial - Industrial</p>
    <ul class="services">
      <li>Electrical</li>
      <li>Data Communications</li>
      <li>Air-conditioning</li>
      <li>CCTV / Security</li>
    </ul>
    <p class="contact">Ph:&nbsp; 0418 362 927<br>Website:&nbsp; www.ktwelec.example.com.au</p>
  </section>
</main>
</body>
</html>
```